Veltrano - Mechanic/Collision Center Business Card

We're looking for a business card design for our mechanic/ collision repair shop.

Can be with colours or monochromatic.

See the attached files.

Many thanks

```html
<!DOCTYPE html>
<html lang="en">
<head>
<meta charset="utf-8">
<title>Veltrano – Business Card</title>
<link rel="stylesheet" href="https://fonts.googleapis.com/css2?family=Open+Sans:wght@400;700&display=swap">
<style>
  :root {
    --backdrop: #3a3a37;
    --card: #121212;
    --card-edge: #1c1c1c;
    --gloss: #2c2c2c;
    --ink: #f2f2f2;
    --ink-soft: #d9d9d9;
  }
  * { box-sizing: border-box; margin: 0; padding: 0; }
  html, body {
    width: 1200px; height: 825px; overflow: hidden;
    background: var(--backdrop);
    font-family: "Open Sans", Arial, sans-serif;
  }
  .stage {
    width: 1200px; height: 825px;
    display: flex; align-items: center; justify-content: center; gap: 50px;
  }
  .card {
    width: 530px; height: 303px;
    background: var(--card);
    border: 1px solid var(--card-edge);
    border-radius: 4px;
    position: relative;
    box-shadow: 0 10px 30px rgba(0,0,0,.45);
  }
  /* front */
  .card-front { display: flex; align-items: center; justify-content: center; }
  .front-brand {
    display: flex; align-items: center; gap: 14px;
    color: var(--gloss);
    font-weight: 700; font-size: 46px; letter-spacing: 2px; text-transform: uppercase;
  }
  .front-brand .mark { width: 22px; height: 22px; background: var(--gloss); }
  /* back */
  .card-back { display: flex; align-items: center; padding: 0 36px; gap: 34px; }
  .back-brand {
    display: flex; align-items: center; gap: 10px;
    color: var(--ink);
    font-weight: 700; font-size: 26px; letter-spacing: 1px; text-transform: uppercase;
    flex: 0 0 auto;
  }
  .back-brand .mark { width: 14px; height: 14px; background: var(--ink); }
  .contact { color: var(--ink-soft); font-size: 12.5px; line-height: 1.55; }
  .contact .person { color: var(--ink); font-size: 17px; line-height: 1.2; }
  .contact .mobile { font-size: 10.5px; margin-bottom: 6px; }
  .contact-row { display: flex; align-items: flex-start; gap: 8px; }
  .contact-row svg { width: 11px; height: 11px; flex: 0 0 11px; margin-top: 4px; fill: var(--ink-soft); }
  .contact-row .plain-square { width: 10px; height: 10px; flex: 0 0 10px; margin-top: 4px; background: var(--ink-soft); }
</style>
</head>
<body>
<main class="stage">
  <section class="card card-front" aria-label="Card front">
    <div class="front-brand"><span class="mark"></span>Veltrano</div>
  </section>

  <section class="card card-back" aria-label="Card back">
    <div class="back-brand"><span class="mark"></span>Veltrano</div>
    <div class="contact">
      <p class="person">Tiago Moreira</p>
      <p class="mobile">+351 912004817 (or just 912004817)</p>
      <div class="contact-row">
        <svg viewBox="0 0 12 12" aria-hidden="true"><path d="M6 0a4 4 0 0 0-4 4c0 3 4 8 4 8s4-5 4-8a4 4 0 0 0-4-4zm0 5.6a1.6 1.6 0 1 1 0-3.2 1.6 1.6 0 0 1 0 3.2z"/></svg>
        <p>Rua das Oficinas, 42<br>1900-418 Lisboa</p>
      </div>
      <div class="contact-row">
        <svg viewBox="0 0 12 12" aria-hidden="true"><path d="M1 3c0-1 1-2 5-2s5 1 5 2v1H8.5V3h-5v1H1zM2 5h8l1 6H1z"/></svg>
        <p>+351 213305924 (or just 213305924)</p>
      </div>
      <div class="contact-row">
        <svg viewBox="0 0 12 12" aria-hidden="true"><path d="M0 2h12v8H0zm1 1v.4l5 3.4 5-3.4V3z"/></svg>
        <p>veltrano.mail@example.com</p>
      </div>
      <div class="contact-row">
        <span class="plain-square"></span>
        <p>www.social.example/veltrano</p>
      </div>
    </div>
  </section>
</main>
</body>
</html>
```